Velvo Gifts Box

Velvo Gifts is a new company selling Experience Gifts. We want to create a unique gift pack that will be sent to the gift recipient containing information about the chosen experience.
We have selected a box style (see movie attached). The exact size of the box is:
Width: 16.2 cm
Height: 3,81 cm
Length: 23.8 cm
Our logo and strapline are attached. We hope to use the words 'Adventure Unwrapped' (our slogan) in a creative way on the packaging or as part of the box opening experience. We prefer something minimalist, clever - black is our preferred packaging color. But we are open to suggestions. We can print directly onto the box. We can also add a seal, stickers, a sleeve or any other graphic addition that would create a premium box and make receiving this gift pack a memorable moment.

```html
<!DOCTYPE html>
<html lang="en">
<head>
<meta charset="utf-8">
<title>Velvo Gifts Box – Sleeve Packaging</title>
<link rel="stylesheet" href="https://fonts.googleapis.com/css2?family=Orbitron:wght@900&family=Exo+2:wght@300&family=Permanent+Marker&family=Arimo:wght@700&display=swap">
<style>
  :root {
    --page: #ffffff;
    --box: #000000;
    --sleeve: #5b5b5b;
    --logo-faint: #3a3a3a;
    --logo-light: #dcdcdc;
    --rope: #bdbdbd;
    --ink: #ffffff;
    --label: #222222;
  }
  html, body {
    margin: 0;
    padding: 0;
    width: 1200px;
    height: 2186px;
    overflow: hidden;
    background: var(--page);
  }
  .canvas {
    position: relative;
    width: 1200px;
    height: 2186px;
  }
  .brand-mark {
    position: absolute;
    font-family: "Orbitron", sans-serif;
    font-weight: 900;
    line-height: 1.08;
    letter-spacing: -1px;
    margin: 0;
  }
  .brand-mark--page { left: 46px; top: 54px; font-size: 50px; color: var(--logo-light); }
  .stage-label {
    position: absolute;
    right: 206px;
    font-family: "Exo 2", sans-serif;
    font-weight: 300;
    font-size: 36px;
    color: var(--label);
    margin: 0;
  }
  .stage-label--before { top: 186px; }
  .stage-label--after { top: 808px; }

  .box {
    position: absolute;
    background: var(--box);
    overflow: hidden;
  }
  .box--before { left: 196px; top: 240px; width: 808px; height: 552px; }
  .box--after { left: 196px; top: 866px; width: 808px; height: 551px; }

  .box .brand-mark { left: 20px; top: 34px; font-size: 60px; color: var(--logo-faint); }

  .sleeve {
    position: absolute;
    left: 393px;
    top: 0;
    width: 79px;
    height: 100%;
    background: var(--sleeve);
  }
  .sleeve__guide {
    position: absolute;
    bottom: 10px;
    width: 100%;
    text-align: center;
    font-family: "Permanent Marker", sans-serif;
    font-size: 14px;
    color: var(--ink);
  }
  .seal-sticker {
    position: absolute;
    left: 380px;
    top: 76px;
    width: 103px;
    height: 102px;
    border: 2px solid var(--ink);
    border-radius: 4px;
    background: var(--box);
    display: flex;
    flex-direction: column;
    justify-content: center;
    align-items: center;
    font-family: "Orbitron", sans-serif;
    font-weight: 900;
    font-size: 19px;
    line-height: 1.1;
    color: var(--ink);
  }
  .rope {
    position: absolute;
    left: 0;
    width: 100%;
    height: 5px;
    background: var(--rope);
  }
  .rope--before { top: 280px; }
  .rope-knot {
    position: absolute;
    left: 392px;
    top: 266px;
    width: 80px;
    height: 32px;
    border-radius: 16px;
    background: linear-gradient(#d0d0d0, #8a8a8a);
  }
  .rope--after-left { top: 279px; width: 404px; }
  .rope--after-right { top: 279px; left: 417px; width: 391px; }
  .globe-art {
    position: absolute;
    left: 396px;
    top: 164px;
    width: 76px;
    height: 110px;
    border-radius: 38px 38px 6px 6px;
    background: radial-gradient(circle at 50% 55%, #ffffff 0%, #9a9a9a 45%, #1a1a1a 80%);
  }
  .slogan {
    position: absolute;
    top: 308px;
    margin: 0;
    font-family: "Orbitron", sans-serif;
    font-weight: 900;
    font-size: 36px;
    letter-spacing: 2px;
    color: var(--ink);
    white-space: nowrap;
  }
  .slogan--left { right: 426px; }
  .slogan--right { left: 476px; }
  .slogan--full { left: 0; width: 100%; text-align: center; }

  .box--diagram { left: 215px; top: 1670px; width: 560px; height: 382px; }
  .box--diagram .brand-mark { left: 14px; top: 20px; font-size: 42px; }
  .box--diagram .sleeve { left: 273px; width: 56px; }
  .box--diagram .sleeve__guide { font-size: 10px; bottom: 6px; }
  .box--diagram .seal-sticker { left: 263px; top: 52px; width: 71px; height: 72px; font-size: 13px; }
  .box--diagram .rope { top: 194px; height: 4px; }
  .box--diagram .rope-knot { left: 272px; top: 184px; width: 56px; height: 22px; }
  .box--diagram .slogan { top: 214px; font-size: 25px; letter-spacing: 1px; }
  .box--diagram .slogan--left { right: 297px; }
  .box--diagram .slogan--right { left: 330px; }

  .callout {
    position: absolute;
    font-family: "Arimo", sans-serif;
    font-weight: 700;
    font-size: 9px;
    color: var(--ink);
  }
  .callout--sleeve { left: 304px; top: 18px; }
  .callout--seal { left: 300px; top: 112px; }
  .callout--rope { left: 521px; top: 184px; }
  .callout--guide { left: 300px; top: 356px; }
  .callout--logo { left: 146px; top: 30px; }

  .legend {
    position: absolute;
    left: 866px;
    top: 1814px;
    margin: 0;
    padding-left: 0;
    list-style: none;
    font-family: "Arimo", sans-serif;
    font-weight: 700;
    font-size: 14px;
    line-height: 17px;
    color: var(--label);
  }
</style>
</head>
<body>
<main class="canvas">
  <p class="brand-mark brand-mark--page">VELVO<br>GIFTS</p>

  <h2 class="stage-label stage-label--before">Before</h2>
  <section class="box box--before">
    <p class="brand-mark">VELVO<br>GIFTS</p>
    <div class="rope rope--before" role="img" aria-label="Printed rope line around the box"></div>
    <p class="slogan slogan--left">ADVENTURE</p>
    <p class="slogan slogan--right">WRAPPED</p>
    <div class="sleeve"><span class="sleeve__guide">SLIDE ME</span></div>
    <div class="rope-knot" role="img" aria-label="Printed rope knot on the sleeve"></div>
    <div class="seal-sticker"><span>VELVO</span><span>GIFTS</span></div>
  </section>

  <h2 class="stage-label stage-label--after">After</h2>
  <section class="box box--after">
    <p class="brand-mark">VELVO<br>GIFTS</p>
    <div class="globe-art" role="img" aria-label="White line illustration of a globe with plane and mountains above the web address www.velvogifts.com"></div>
    <div class="rope rope--after-left" role="img" aria-label="Printed rope line, left part"></div>
    <div class="rope rope--after-right" role="img" aria-label="Printed rope line, right part"></div>
    <p class="slogan slogan--full">ADVENTURE UNWRAPPED</p>
  </section>

  <section class="box box--diagram">
    <p class="brand-mark">VELVO<br>GIFTS</p>
    <span class="callout callout--logo">5</span>
    <div class="rope" role="img" aria-label="Printed rope line around the box"></div>
    <span class="callout callout--rope">3</span>
    <p class="slogan slogan--left">ADVENTURE</p>
    <p class="slogan slogan--right">WRAPPED</p>
    <div class="sleeve"><span class="sleeve__guide">SLIDE ME</span></div>
    <span class="callout callout--sleeve">1</span>
    <span class="callout callout--guide">4</span>
    <div class="rope-knot" role="img" aria-label="Printed rope knot on the sleeve"></div>
    <div class="seal-sticker"><span>VELVO</span><span>GIFTS</span></div>
    <span class="callout callout--seal">2</span>
  </section>

  <ol class="legend">
    <li>1. Box Sleeve</li>
    <li>2. Sticker with company logo as sleeve seal</li>
    <li>3. ‘Rope’ Print</li>
    <li>4. Sleeve guide - optional</li>
    <li>5. Company logo</li>
  </ol>
</main>
</body>
</html>
```